Business Stationery design
Letterhead, compliments slip, business card x 2, email signature
Business Stationery design - Health
Creative Brief
A new design of letterhead required following our rebranding excercise which started with a new logo
Health
Patients, corporate
1. We require a letterhead for A4 paper, this must be contemporary and modern in design using the logo attached somewhere in the design. 2. We require a design for a compliments slip 99mm x 210mm, this can be portrait or landscape, using the logo attached and reflecting the design of the letterhead. 3. We require 2 designs of business cards - one which will be printed on clear plastic and one will be on card, the card one can be double sided. The information for the business card is a follows: Roderick Penhale B.Sc., MCOptom, F.B.D.O., Dip.O.D., OPwSI Ophthalmology Senior Consultant Optometrist The business information for all three is: Address: 14 Tarrow Lane, Snodland, Kent ME4 2QX Telephone: 01632 918372 Email: info@clearviewsample.co.uk Web Address: www.clearviewsample.co.uk Additional information for the letterhead which can be 8pt: Registered Office: Harlow Penrose Judd, Brenton House, Vell Street, Dover, Kent CT12 7RW Company Registered in England and Wales: 09381726 Finally - 4: an email signature using the logo address etc
Roderick Roderick
OK, again great designs but no-one seems to have listened the the problem that we cannot have a bleed on the A4 paper. It is probably therefore best to have 2 designs for the A4 paper - one with a bleed and one without. This is because we do have some A4 paper printed and some is printed as a mailshot is done by an outside source and they do not have the ability to bleed off the edge of the paper - please modify your designs
Thank you all for your designs, design No 24 has the correct formatting for the name and qualifications etc which should be Roderick Penhale B.Sc., MCOptom., F.B.D.O., Dip.O.D., OPwSI Ophthalmology Senior Consultant Optometrist (copy and paste the above and the lines etc should be correct) At the moment I favour design 16. I think that the curves have been done to death by every company so we need to stay away from that now please unless you have something cutting edge and amazing! Many thanks
Also the letterhead cannot include a bleed, unless you do a design with and without a bleed as some mailings are printed and mailed offsite and they do not have the ability to bleed at present
OK designs are looking good so far, I have rated them. However I want to lose the corporate look a little as we are an independent practice. Also the formatting for the name, qualifications etc should be: Roderick Penhale B.Sc., MCOPtom., F.B.D.O., Dip.O.D., OPwSI Ophthalmology Senior Consultant Optometrist

```html
<!DOCTYPE html>
<html lang="en">
<head>
<meta charset="utf-8">
<title>Clearview Optometrists – Business Stationery</title>
<link href="https://fonts.googleapis.com/css2?family=PT+Sans:wght@400;700&family=Dancing+Script:wght@600&display=swap" rel="stylesheet">
<style>
  :root{
    --backdrop:#e6e2dd;
    --paper:#ffffff;
    --navy:#1d3a7a;
    --blue:#2750a8;
    --blue-deep:#142a66;
    --ink:#2b2b2b;
    --grey:#8a8d93;
    --silver:#c9cbcf;
    --clear:rgba(214,200,190,0.75);
  }
  *{box-sizing:border-box;margin:0;padding:0}
  html,body{width:1200px;height:900px;overflow:hidden}
  body{background:var(--backdrop);font-family:"PT Sans",Arial,sans-serif;color:var(--ink);position:relative}
  .piece{position:absolute;background:var(--paper);box-shadow:0 2px 6px rgba(0,0,0,.18);overflow:hidden}
  .tab{position:absolute;top:0;height:8px;background:linear-gradient(var(--silver),#e9eaec)}
  .bar{position:absolute;right:0;bottom:0;height:14px;background:linear-gradient(90deg,var(--blue),var(--blue-deep));color:#fff;font-size:7px;line-height:14px;padding:0 10px;text-align:right;white-space:nowrap}
  .brand{position:absolute;display:flex;align-items:flex-start;gap:6px;color:var(--navy);font-weight:400;line-height:1}
  .brand .dot{border-radius:50%;background:var(--navy);flex:none}
  .brand .name{display:block}
  .brand .sub{display:block;letter-spacing:.12em}
  .holder{position:absolute;line-height:1.25}
  .holder .person{font-size:13px;color:var(--navy)}
  .holder .quals,.holder .role{font-size:5.5px;color:var(--grey)}
  .contact{position:absolute;font-size:5.5px;color:var(--grey);line-height:1.5;white-space:nowrap}

  .card-clear{left:61px;top:139px;width:220px;height:154px;background:var(--clear);border-radius:10px}
  .card-back{left:366px;top:68px;width:215px;height:132px;background:radial-gradient(circle at 60% 30%,var(--blue),var(--blue-deep));border-radius:8px}
  .card-back .brand{color:#fff}
  .card-back .brand .dot{background:#fff}
  .card-back .bar{background:#fff;color:var(--navy);right:10px;bottom:10px;width:110px;height:11px;line-height:11px;border-radius:2px}
  .card-front{left:366px;top:215px;width:215px;height:120px;border-radius:8px}
  .slip{left:61px;top:366px;width:520px;height:249px}
  .slip .greeting{position:absolute;right:24px;bottom:26px;font-family:"Dancing Script",cursive;font-size:30px;color:var(--ink)}
  .signature{left:256px;top:647px;width:325px;height:154px}
  .letterhead{left:617px;top:68px;width:517px;height:737px}
  .registered{position:absolute;left:0;right:0;top:620px;text-align:center;font-size:6px;color:var(--grey);line-height:1.5}
  .lh-contact{position:absolute;left:0;right:0;top:670px;text-align:center;font-size:7px;color:var(--ink);line-height:1.7}
  .lh-contact svg{vertical-align:-1px;margin-right:3px}
</style>
</head>
<body>

<div class="piece card-clear">
  <div class="brand" style="left:14px;top:16px">
    <span class="dot" style="width:12px;height:12px"></span>
    <span><span class="name" style="font-size:17px">Clearview</span><span class="sub" style="font-size:6px">OPTOMETRISTS</span></span>
  </div>
  <div class="holder" style="left:90px;top:54px">
    <div class="person">Roderick Penhale</div>
    <div class="quals">B.Sc., MCOptom., F.B.D.O., Dip.O.D., OPwSI</div>
    <div class="role">Ophthalmology Senior Consultant Optometrist</div>
  </div>
  <div class="contact" style="left:90px;top:92px">14 Tarrow Lane, Ashcombe, Eastvale ME4 2QX<br>01632 918372 · info@clearviewsample.co.uk</div>
  <div class="bar" style="bottom:14px;right:10px;width:100px;border-radius:2px">www.clearviewsample.co.uk</div>
</div>

<div class="piece card-back">
  <div class="brand" style="left:40px;top:36px">
    <span class="dot" style="width:14px;height:14px"></span>
    <span><span class="name" style="font-size:20px">Clearview</span><span class="sub" style="font-size:7px">OPTOMETRISTS</span></span>
  </div>
  <div class="bar">www.clearviewsample.co.uk</div>
</div>

<div class="piece card-front">
  <div class="brand" style="left:14px;top:14px">
    <span class="dot" style="width:10px;height:10px"></span>
    <span><span class="name" style="font-size:15px">Clearview</span><span class="sub" style="font-size:5px">OPTOMETRISTS</span></span>
  </div>
  <div class="holder" style="left:80px;top:36px">
    <div class="person">Roderick Penhale</div>
    <div class="quals">B.Sc., MCOptom., F.B.D.O., Dip.O.D., OPwSI</div>
    <div class="role">Ophthalmology Senior Consultant Optometrist</div>
  </div>
  <div class="contact" style="left:14px;top:80px">14 Tarrow Lane, Ashcombe, Eastvale ME4 2QX<br>01632 918372 · info@clearviewsample.co.uk</div>
  <div class="bar" style="width:110px">www.clearviewsample.co.uk</div>
</div>

<div class="piece slip">
  <div class="tab" style="left:250px;width:40px"></div>
  <div class="brand" style="left:26px;top:34px">
    <span class="dot" style="width:16px;height:16px"></span>
    <span><span class="name" style="font-size:24px">Clearview</span><span class="sub" style="font-size:8px">OPTOMETRISTS</span></span>
  </div>
  <div class="greeting">With Compliments</div>
  <div class="bar" style="width:150px;height:10px;line-height:10px;font-size:6px">www.clearviewsample.co.uk</div>
</div>

<div class="piece signature">
  <div class="tab" style="left:115px;width:60px"></div>
  <div class="brand" style="left:118px;top:16px">
    <span class="dot" style="width:10px;height:10px"></span>
    <span><span class="name" style="font-size:14px">Clearview</span><span class="sub" style="font-size:5px">OPTOMETRISTS</span></span>
  </div>
  <div class="holder" style="left:0;right:0;top:52px;text-align:center">
    <div class="person">Roderick Penhale</div>
    <div class="quals">B.Sc., MCOptom., F.B.D.O., Dip.O.D., OPwSI</div>
    <div class="role">Ophthalmology Senior Consultant Optometrist</div>
  </div>
  <div class="contact" style="left:0;right:0;top:96px;text-align:center">www.clearviewsample.co.uk<br>14 Tarrow Lane, Ashcombe, Eastvale ME4 2QX<br>01632 918372 · info@clearviewsample.co.uk</div>
  <div class="bar" style="width:140px;height:10px;line-height:10px;font-size:6px">www.clearviewsample.co.uk</div>
</div>

<div class="piece letterhead">
  <div class="tab" style="left:60px;width:70px"></div>
  <div class="brand" style="left:60px;top:30px">
    <span class="dot" style="width:18px;height:18px"></span>
    <span><span class="name" style="font-size:28px">Clearview</span><span class="sub" style="font-size:9px">OPTOMETRISTS</span></span>
  </div>
  <div class="registered">Registered Office: Harlow Penrose Judd, Brenton House, Vell Street, Harbridge, Eastvale CT12 7RW<br>Company Registered in England and Wales: 09381726</div>
  <div class="lh-contact">
    <div><svg width="7" height="8" viewBox="0 0 7 8"><path d="M3.5 0A3 3 0 0 0 .5 3c0 2.2 3 5 3 5s3-2.8 3-5a3 3 0 0 0-3-3z" fill="#2b2b2b"/></svg>14 Tarrow Lane, Ashcombe, Eastvale ME4 2QX</div>
    <div><svg width="7" height="7" viewBox="0 0 7 7"><path d="M1 0h1.5l.7 1.8-.9.7a4 4 0 0 0 2.2 2.2l.7-.9L7 4.5V6a1 1 0 0 1-1 1A6 6 0 0 1 0 1a1 1 0 0 1 1-1z" fill="#2b2b2b"/></svg>01632 918372</div>
  </div>
  <div class="contact" style="right:14px;top:678px;font-size:6px;color:var(--ink)">info@clearviewsample.co.uk</div>
  <div class="bar" style="width:140px;height:16px;line-height:16px;bottom:18px">www.clearviewsample.co.uk</div>
</div>

</body>
</html>
```